BrightNomadRx.com Blog Design (Travel, Lifestyle, and Life Hacking blog)

I am launching a lifestyle blog about my life. I'm a doctor who travels the world trying the best restaurants, airlines and trying to have as much fun as possible. I also invest in startups, and am always trying new tricks to make life better. I also plan to write about various other topics, but essentially it is about travel, lifestyle and medicine. I need a creative and really awesome looking design for a new wordpress blog called BrightNomadRx

Target Market(s)

Physicians, Entrepreneurs, Travellers

Industry/Entity Type

Airlines

Number of Pages Required

1 page

Font styles to use
Serif

Requirements
Must have
• Slick looking graphics with a highly professional modern feel

```html
<!DOCTYPE html>
<html lang="en">
<head>
<meta charset="utf-8">
<title>BrightNomadRx — Travel, Lifestyle &amp; Medicine</title>
<link href="https://fonts.googleapis.com/css2?family=Montserrat:wght@400;600;700&family=Open+Sans:wght@400;600&display=swap" rel="stylesheet">
<style>
  :root {
    --ink: #111111;
    --black: #000000;
    --white: #ffffff;
    --muted: #8a8a8a;
    --text: #6f6f6f;
    --rule: #cfcfcf;
    --input-line: #bdbdbd;
  }
  * { box-sizing: border-box; margin: 0; padding: 0; }
  html, body { width: 1200px; height: 4245px; overflow: hidden; }
  body {
    position: relative;
    background: var(--white);
    color: var(--ink);
    font-family: "Open Sans", Arial, sans-serif;
  }
  .abs { position: absolute; }
  .heading { font-family: "Montserrat", Arial, sans-serif; font-weight: 700; text-transform: uppercase; color: var(--ink); }

  /* Navigation */
  .site-nav { left: 0; top: 0; width: 1200px; height: 42px; background: var(--black); }
  .brand { left: 212px; top: 0; height: 42px; line-height: 42px; color: var(--white); font-family: "Montserrat", sans-serif; font-weight: 700; font-size: 14px; letter-spacing: .3px; white-space: nowrap; }
  .nav-links { left: 0; top: 0; width: 1200px; height: 42px; list-style: none; }
  .nav-links li { position: absolute; top: 0; line-height: 42px; color: var(--white); font-family: "Montserrat", sans-serif; font-size: 9.5px; font-weight: 600; letter-spacing: .4px; white-space: nowrap; }
  .social { left: 862px; top: 17px; display: flex; gap: 12px; }
  .social span { width: 8px; height: 8px; border-radius: 50%; background: var(--white); display: block; }
  .search { left: 976px; top: 14px; }

  /* Hero */
  .hero-photo { left: 212px; top: 91px; width: 776px; height: 376px; background: linear-gradient(180deg, #f0b456 0%, #d98b3a 45%, #6b4a3a 72%, #cfd3d6 100%); }
  .hero-card { left: 362px; top: 360px; width: 476px; height: 300px; background: var(--white); border: 1px solid #e4e4e4; text-align: center; }
  .hero-card h1 { position: absolute; left: 0; top: 28px; width: 100%; font-size: 31px; line-height: 40px; letter-spacing: .5px; }
  .hero-date { position: absolute; left: 0; top: 112px; width: 100%; font-size: 9px; color: var(--muted); text-decoration: underline; letter-spacing: .5px; }
  .hero-excerpt { position: absolute; left: 80px; top: 146px; width: 316px; font-size: 9.5px; line-height: 14px; color: var(--muted); }
  .btn-outline { position: absolute; left: 168px; top: 229px; width: 140px; height: 33px; border: 1px solid var(--ink); font-family: "Montserrat", sans-serif; font-size: 8.5px; font-weight: 700; line-height: 31px; letter-spacing: .5px; }

  /* Category tiles */
  .tile { top: 710px; width: 236px; height: 207px; }
  .tile-label { position: absolute; left: 68px; top: 91px; width: 100px; height: 24px; background: var(--white); font-family: "Montserrat", sans-serif; font-size: 8.5px; font-weight: 700; text-align: center; line-height: 24px; text-transform: uppercase; }
  .tile-medical { left: 212px; background: linear-gradient(135deg, #f4f4f4 0%, #d8e3ef 55%, #3d6fb0 100%); }
  .tile-lifestyle { left: 481px; background: linear-gradient(135deg, #2a2420 0%, #8e6a4f 55%, #1d1a18 100%); }
  .tile-travel { left: 750px; background: linear-gradient(180deg, #f7f1d8 0%, #efe3b4 60%, #d9b77a 100%); }

  /* Feature posts */
  .post-cat { left: 212px; width: 776px; text-align: center; font-family: "Montserrat", sans-serif; font-size: 9px; font-weight: 700; text-decoration: underline; letter-spacing: .5px; }
  .post-title { left: 212px; width: 776px; text-align: center; font-size: 27px; line-height: 32px; letter-spacing: .3px; }
  .post-photo { left: 212px; width: 776px; height: 348px; }
  .photo-wall { background: linear-gradient(180deg, #3a3a3a 0%, #d9d9d9 12%, #cfcfcf 70%, #8e8e8e 100%); }
  .photo-food { background: linear-gradient(90deg, #6b4a2f 0%, #8b5e3a 35%, #efe9e2 55%, #d86a2e 72%, #f1ebe4 100%); }
  .post-body { left: 212px; width: 776px; font-size: 11px; line-height: 15.5px; color: var(--text); }
  .post-meta { left: 212px; width: 776px; height: 43px; }
  .meta-text { position: absolute; top: 14px; font-family: "Montserrat", sans-serif; font-size: 9.5px; font-weight: 600; color: var(--ink); text-transform: uppercase; }
  .btn-solid { position: absolute; left: 261px; top: 0; width: 223px; height: 43px; background: var(--black); color: var(--white); font-family: "Montserrat", sans-serif; font-size: 9.5px; font-weight: 700; text-align: center; line-height: 43px; letter-spacing: .4px; }

  /* Ad */
  .ad-banner { left: 212px; top: 2640px; width: 776px; height: 198px; background: linear-gradient(180deg, #1f1f22 0%, #4b4d52 40%, #6e6f73 60%, #2a2a2d 100%); }
  .ad-frame { position: absolute; left: 20px; top: 20px; width: 736px; height: 158px; border: 1px solid rgba(255,255,255,.8); color: var(--white); font-family: "Montserrat", sans-serif; font-size: 31px; font-weight: 600; text-align: center; line-height: 156px; letter-spacing: 1px; }

  /* Grid posts */
  .card { width: 365px; text-align: center; }
  .card-photo { height: 218px; }
  .card-cat { margin-top: 26px; font-family: "Montserrat", sans-serif; font-size: 8px; font-weight: 600; text-decoration: underline; color: var(--text); }
  .card-title { margin-top: 11px; font-family: "Montserrat", sans-serif; font-size: 17.5px; font-weight: 400; text-transform: uppercase; letter-spacing: .3px; white-space: nowrap; }
  .card-btn { display: inline-block; margin-top: 8px; width: 122px; height: 23px; background: var(--black); color: var(--white); font-family: "Montserrat", sans-serif; font-size: 8px; font-weight: 700; line-height: 23px; }
  .ph-cake { background: linear-gradient(135deg, #ffffff 0%, #f2e7e4 40%, #c9202f 65%, #3b2b5a 100%); }
  .ph-wing { background: linear-gradient(180deg, #7fa6d4 0%, #c9dcef 50%, #f4f6f9 100%); }
  .ph-office { background: linear-gradient(135deg, #d7d9da 0%, #f3f3f3 50%, #7a6152 100%); }
  .ph-medicine { background: linear-gradient(135deg, #8a5a35 0%, #b07a4b 45%, #c9d39a 65%, #8a5a35 100%); }

  .load-more { left: 212px; top: 3707px; width: 776px; height: 46px; border-top: 1px solid var(--rule); border-bottom: 1px solid var(--rule); text-align: center; line-height: 44px; font-family: "Montserrat", sans-serif; font-size: 10px; font-weight: 600; }

  /* Newsletter */
  .news-title { left: 0; top: 3820px; width: 1200px; text-align: center; font-size: 31px; }
  .news-sub { left: 0; top: 3860px; width: 1200px; text-align: center; font-family: "Montserrat", sans-serif; font-size: 9px; font-weight: 700; text-transform: uppercase; }
  .news-form { left: 402px; top: 3905px; width: 410px; height: 43px; border: 1px solid var(--input-line); }
  .news-input { position: absolute; left: 14px; top: 0; line-height: 41px; font-size: 9px; color: #b0b0b0; letter-spacing: .5px; }
  .news-go { position: absolute; right: 0; top: 0; width: 59px; height: 41px; border-left: 1px solid var(--input-line); text-align: center; line-height: 41px; font-family: "Montserrat", sans-serif; font-size: 10px; font-weight: 700; }

  /* Instagram strip */
  .insta { left: 0; top: 4041px; width: 1200px; height: 204px; display: flex; }
  .insta div { flex: 1; height: 100%; }
  .ig1 { background: linear-gradient(135deg, #f7f7f7, #eee7de); }
  .ig2 { background: linear-gradient(135deg, #f4f2ee, #e9e4dc); }
  .ig3 { background: linear-gradient(135deg, #ece6de, #d7cbbf); }
  .ig4 { background: linear-gradient(180deg, #c8893b 0%, #8c3b1e 45%, #6aa03a 60%, #d99a3f 100%); }
  .ig5 { background: linear-gradient(135deg, #dfe9ef 0%, #bcd3e0 50%, #f2f2f2 100%); }
  .ig6 { background: linear-gradient(135deg, #e9efe2 0%, #7f9b5c 60%, #4f6b38 100%); }
  .insta-label { left: 262px; top: 4140px; font-family: "Montserrat", sans-serif; font-size: 15px; font-weight: 600; letter-spacing: 1.5px; color: #333; }
</style>
</head>
<body>

<header class="abs site-nav">
  <div class="abs brand">BrightNomadRx</div>
  <ul class="abs nav-links">
    <li style="left:370px">MEDICAL</li>
    <li style="left:438px">LIFESTYLE</li>
    <li style="left:511px">TRAVEL</li>
    <li style="left:571px">FOOD</li>
    <li style="left:627px">START UP</li>
    <li style="left:695px">BUSINESS</li>
    <li style="left:765px">ABOUT</li>
  </ul>
  <div class="abs social" aria-label="Social links"><span></span><span></span><span></span><span></span><span></span><span></span></div>
  <svg class="abs search" width="14" height="14" viewBox="0 0 14 14" aria-label="Search"><circle cx="6" cy="6" r="4.2" fill="none" stroke="#fff" stroke-width="1.5"/><line x1="9" y1="9" x2="12.5" y2="12.5" stroke="#fff" stroke-width="1.5"/></svg>
</header>

<section>
  <div class="abs hero-photo" role="img" aria-label="Man in a shirt and tie surfing a wave at sunset"></div>
  <article class="abs hero-card">
    <h1 class="heading">Be Courageous to<br>Surfing</h1>
    <div class="hero-date">NOVEMBER 20, 2016</div>
    <p class="hero-excerpt">A short morning session on the water taught me more about fear than any lecture. Here is how a busy doctor learned to paddle out, fall often and keep getting back up on the board.</p>
    <div class="btn-outline">CONTINUE READING</div>
  </article>
</section>

<nav>
  <div class="abs tile tile-medical" role="img" aria-label="Doctor holding a blue clipboard with a stethoscope"><span class="tile-label">Medical</span></div>
  <div class="abs tile tile-lifestyle" role="img" aria-label="Hand holding a coffee cup"><span class="tile-label">Lifestyle</span></div>
  <div class="abs tile tile-travel" role="img" aria-label="Traveller with a backpack in a bright landscape"><span class="tile-label">Traveling</span></div>
</nav>

<article>
  <div class="abs post-cat" style="top:1018px">LIFESTYLE</div>
  <h2 class="abs heading post-title" style="top:1053px">Under $100 DIY: Turn Your Living Room Into<br>a Major Style Statement</h2>
  <div class="abs post-photo photo-wall" style="top:1152px" role="img" aria-label="White room with a wall of empty white picture frames"></div>
  <p class="abs post-body" style="top:1546px">Redecorating does not have to drain your savings. With a few thrifted frames, a can of matte white paint and one free weekend, a plain wall can become the calm, gallery-style centrepiece of your living room. Start by laying every frame on the floor and moving them around until the spacing feels balanced, then trace each shape onto paper and tape the templates to the wall. Paint the frames the same shade as the wall so texture, not colour, does the talking. Add soft warm bulbs above, keep the floor bare and light, and let the room breathe. Mix large and small frames so the eye keeps moving, leave a wider gap around the centre piece, and check the layout from across the room before you drill a single hole. A level, a pencil and a little patience matter more than any expensive tool. The whole project came in well under one hundred dollars and took just two afternoons of easy, relaxed work, and the result still makes every guest stop and look twice.</p>
  <div class="abs post-meta" style="top:1692px">
    <span class="meta-text" style="left:0">12 Comments</span>
    <span class="btn-solid">CONTINUE READING</span>
    <span class="meta-text" style="right:0">Share</span>
  </div>
</article>

<article>
  <div class="abs post-cat" style="top:1828px">FOOD</div>
  <h2 class="abs heading post-title" style="top:1863px">9 Ideas for Your Next Outdoor<br>Party Food</h2>
  <div class="abs post-photo photo-food" style="top:1964px" role="img" aria-label="Grilled chicken with lemon slices and basil on a white plate beside a fork"></div>
  <p class="abs post-body" style="top:2356px">Summer evenings call for food that is easy to share and hard to forget. These nine ideas lean on fresh herbs, bright citrus and simple grilling so you spend more time with guests and less time at the stove. Marinate chicken thighs in lemon, garlic and smoked paprika, then sear them hot for crisp edges. Build a board of seasonal fruit, soft cheese and crunchy bread. Keep a pitcher of mint water cold and a bowl of salted almonds close by. Grill halved peaches for dessert, toss corn with lime and chilli, and set out small bowls of yogurt dip with cucumber and dill. Skewers are your friend: they cook fast, need no cutlery and let everyone pick their favourites. Every recipe here can be prepared ahead, travels well to a park or beach, and scales easily from four friends to twenty without any extra stress or a long list of shopping.</p>
  <div class="abs post-meta" style="top:2502px">
    <span class="meta-text" style="left:0">12 Comments</span>
    <span class="btn-solid">CONTINUE READING</span>
    <span class="meta-text" style="right:0">Share</span>
  </div>
</article>

<aside class="abs ad-banner" role="img" aria-label="Dark cloudy sky advertisement background">
  <div class="ad-frame">AD BANNER</div>
</aside>

<section>
  <article class="abs card" style="left:212px;top:2923px">
    <div class="card-photo ph-cake" role="img" aria-label="Cake topped with strawberries and blueberries"></div>
    <div class="card-cat">FOOD</div>
    <h3 class="card-title">How to Make Strawberry Cake</h3>
    <span class="card-btn">READ ARTICLE</span>
  </article>
  <article class="abs card" style="left:623px;top:2923px">
    <div class="card-photo ph-wing" role="img" aria-label="Airplane wing above the clouds"></div>
    <div class="card-cat">TRAVEL</div>
    <h3 class="card-title">Travel with Budget Airlines</h3>
    <span class="card-btn">READ ARTICLE</span>
  </article>
  <article class="abs card" style="left:212px;top:3320px">
    <div class="card-photo ph-office" role="img" aria-label="Bright meeting room with a white table and chairs"></div>
    <div class="card-cat">START UP</div>
    <h3 class="card-title">How to Build a Great Workspace</h3>
    <span class="card-btn">READ ARTICLE</span>
  </article>
  <article class="abs card" style="left:623px;top:3320px">
    <div class="card-photo ph-medicine" role="img" aria-label="Bowl of herbal paste with mint leaves on wood"></div>
    <div class="card-cat">MEDICAL</div>
    <h3 class="card-title">Traditional Medicine</h3>
    <span class="card-btn">READ ARTICLE</span>
  </article>
</section>

<div class="abs load-more">LOAD MORE</div>

<section>
  <h2 class="abs heading news-title">Newsletter</h2>
  <p class="abs news-sub">Subscribe my blog, sign up for our weekly newsletter</p>
  <div class="abs news-form">
    <span class="news-input">YOUR E-MAIL ADDRESS</span>
    <span class="news-go">GO</span>
  </div>
</section>

<footer>
  <div class="abs insta">
    <div class="ig1" role="img" aria-label="Soft light interior photo"></div>
    <div class="ig2" role="img" aria-label="Faded kitchen photo"></div>
    <div class="ig3" role="img" aria-label="Neutral lifestyle photo"></div>
    <div class="ig4" role="img" aria-label="Burger close-up"></div>
    <div class="ig5" role="img" aria-label="Clinic scene in soft blue tones"></div>
    <div class="ig6" role="img" aria-label="Green potted herbs"></div>
  </div>
  <div class="abs insta-label">FOLLOW ME ON INSTAGRAM</div>
</footer>

</body>
</html>
```